THE Harrowfield Mobility Fund (HMF) PHOTOGRAPHY COMPETITION

We need a "flyer" (must be web friendly" as well as A5 Print) designed that will announce the launch of a new photography competition. The Theme of the Competition will be "Keep Moving Forward".

Harrowfield Mobility Fund will "host" a competition that is open to all comers, irrespective of experience, but within the following Classes : 1. People Living with Spinal Injuries 2. Schools 3. Amateur Under 18 Photographers 4. Amateur Over 18 Photographers 5. Charities 6. Professional Photographers.

The competition will start in October 2018 and entries will be accepted via the HMF website until 31st August 2019. Prizes to include a Cash Prize of £7,500 for the photograph that in the opinion of the judges best meets the brief. Each Class winner and runner up will receive photographic equipment (a camera for the winner, a tripod for the runner up). The two best photographs in each class will be included in HMF's 2020 Calendar. Prizes will be presented at an event in Salisbury in October 2019.

Entry Fee (payable via the HMF website) will be £2.00 per photograph.

Please note that this is an initial "draft" and any published "flyer / web page will have to meet current UK Charity Regulations.

Telephone +44 (0)1632 960418

www.hmf-example.org.uk (new website to be launched prior to Competition starting)

find us on facebook & twitter

Registered charity No. 1098472

Target Market(s)

Photographers, Schools, Charities

Industry/Entity Type

Charity

Font styles to use
Sans Serif

Colors

Designer to choose colors to be used in the design.

Requirements
Must have
• The HMF Logo
Nice to have
• Less words, high graphic appeal
Should not have
• Any doom and gloom! - People Living with Spinal Injuries are not "sick" - they are "Living With" Spinal Injury - not dieing from it!

```html
<!DOCTYPE html>
<html lang="en">
<head>
<meta charset="utf-8">
<title>Keep Moving Forward – Photography Competition</title>
<link href="https://fonts.googleapis.com/css2?family=Archivo:wght@400;500;600;800;900&display=swap" rel="stylesheet">
<style>
  :root {
    --olive: #8a8972;
    --khaki: #aeab92;
    --beige: #dedbbf;
    --white: #ffffff;
    --ink: #111111;
    --teal: #2fb7c7;
    --page: #e9e9e9;
  }
  * { box-sizing: border-box; margin: 0; padding: 0; }
  html, body { width: 1200px; height: 1200px; overflow: hidden; background: var(--page); }
  body { font-family: "Archivo", Arial, sans-serif; color: var(--ink); position: relative; }

  .flyer {
    position: absolute; left: 190px; top: 20px;
    width: 820px; height: 1160px; overflow: hidden;
    background: var(--olive);
    box-shadow: 0 6px 24px rgba(0,0,0,.18);
  }
  .shape { position: absolute; }
  .shape--beige-back { left: 150px; top: -40px; width: 420px; height: 330px; background: var(--beige); transform: rotate(-8deg); }
  .shape--beige-right { left: 560px; top: 150px; width: 320px; height: 260px; background: var(--beige); transform: rotate(14deg); }
  .shape--olive-right { left: 610px; top: 170px; width: 260px; height: 200px; background: var(--olive); transform: rotate(14deg); }
  .shape--khaki-field { left: 420px; top: 330px; width: 400px; height: 700px; background: var(--khaki); }
  .shape--white-panel { left: 0; top: 330px; width: 440px; height: 680px; background: var(--white); }

  .logo {
    position: absolute; left: 280px; top: 40px; width: 330px; height: 170px;
    background: var(--white); transform: rotate(-4deg);
    display: flex; align-items: center; gap: 18px; padding: 0 26px;
  }
  .logo__mark { width: 46px; height: 46px; border-radius: 50%; background: var(--teal); flex: none; }
  .logo__name {
    font-weight: 500; font-size: 27px; line-height: 1.05; color: #7b7660;
    text-transform: uppercase; letter-spacing: 1px;
  }

  .title { position: absolute; left: 34px; top: 262px; z-index: 3; }
  .title__main { font-weight: 900; font-size: 64px; line-height: 1; letter-spacing: -1px; text-transform: uppercase; }
  .title__sub { font-weight: 600; font-size: 30px; margin-top: 6px; text-transform: uppercase; letter-spacing: .5px; }

  .dates { position: absolute; left: 40px; top: 420px; color: var(--teal); font-weight: 600; font-size: 52px; line-height: 1.02; z-index: 3; }
  .dates sup { font-size: 26px; }

  .intro { position: absolute; left: 40px; top: 560px; width: 380px; font-weight: 600; font-size: 19px; line-height: 1.2; z-index: 3; }
  .classes { list-style: none; margin-top: 14px; font-weight: 500; font-size: 16px; line-height: 1.3; }
  .classes li { position: relative; padding-left: 18px; }
  .classes li::before { content: ""; position: absolute; left: 0; top: 5px; width: 10px; height: 10px; border-radius: 50%; background: var(--teal); }

  .prizes { position: absolute; left: 40px; top: 860px; width: 330px; font-size: 15px; font-weight: 500; line-height: 1.25; z-index: 3; }
  .prizes p + p { margin-top: 6px; }
  .prizes .prizes__event { color: var(--teal); }

  .artwork {
    position: absolute; left: 450px; top: 420px; width: 360px; height: 600px;
    background: linear-gradient(160deg, #d9d6ba 0%, #a9a68c 45%, #2a2a26 100%);
    z-index: 2;
  }

  .fee {
    position: absolute; left: 360px; top: 800px; width: 190px; height: 190px; border-radius: 50%;
    background: var(--teal); color: var(--ink); z-index: 4;
    display: flex; flex-direction: column; align-items: center; justify-content: center; text-align: center;
    transform: rotate(12deg);
  }
  .fee__label { font-weight: 600; font-size: 20px; }
  .fee__amount { font-weight: 900; font-size: 54px; line-height: 1; color: var(--white); }
  .fee__unit { font-weight: 600; font-size: 20px; }
  .fee__note { font-size: 11px; color: var(--white); margin-top: 4px; }

  .footer { position: absolute; left: 0; top: 1010px; width: 820px; height: 150px; background: var(--ink); z-index: 5; }
  .footer__stripe { position: absolute; left: 0; top: -8px; width: 820px; height: 8px; background: var(--teal); }
  .footer__web { position: absolute; left: 40px; top: 24px; color: var(--white); font-weight: 800; font-size: 15px; }
  .footer__charity { position: absolute; left: 40px; top: 44px; color: var(--teal); font-weight: 800; font-size: 15px; }
  .footer__phone { position: absolute; left: 40px; top: 86px; color: var(--white); font-weight: 800; font-size: 34px; display: flex; align-items: center; gap: 14px; }
  .footer__social {
    position: absolute; right: 0; top: 60px; width: 230px; height: 90px; background: var(--teal);
    clip-path: polygon(12% 0, 100% 0, 100% 100%, 0 100%, 0 40%);
    display: flex; align-items: center; justify-content: center; gap: 18px;
  }
  .footer__social span { width: 46px; height: 46px; border-radius: 50%; background: var(--ink); }
</style>
</head>
<body>
  <main class="flyer">
    <div class="shape shape--beige-back"></div>
    <div class="shape shape--beige-right"></div>
    <div class="shape shape--olive-right"></div>
    <div class="shape shape--khaki-field"></div>
    <div class="shape shape--white-panel"></div>

    <div class="logo" aria-label="HMF Logo">
      <span class="logo__mark"></span>
      <span class="logo__name">Harrowfield<br>Mobility<br>Fund</span>
    </div>

    <header class="title">
      <h1 class="title__main">Keep Moving Forward</h1>
      <p class="title__sub">Photography Competition</p>
    </header>

    <p class="dates">Oct 2018 to<br>31<sup>st</sup> Aug 2019</p>

    <section class="intro">
      <p>Competition is open to all comers, irrespective of experience, but within the following Classes:</p>
      <ul class="classes">
        <li>People Living with Spinal Injuries</li>
        <li>Schools</li>
        <li>Amateur Under 18 Photographers</li>
        <li>Amateur Over 18 Photographers</li>
        <li>Charities</li>
        <li>Professional Photographers.</li>
      </ul>
    </section>

    <section class="prizes">
      <p>Each Class winner to receive a camera and runner up to receive a tripod.</p>
      <p>The two best photographs in each class will be included in HMF's 2020 Calendar.</p>
      <p class="prizes__event">Prizes will be presented at an event in Salisbury in October 2019.</p>
    </section>

    <div class="artwork" role="img" aria-label="Grunge silhouette illustration of a camera on a tripod over splattered khaki shapes"></div>

    <div class="fee">
      <span class="fee__label">Entry Fee</span>
      <span class="fee__amount">£2.00</span>
      <span class="fee__unit">per photograph</span>
      <span class="fee__note">Payable via the HMF<br>website</span>
    </div>

    <footer class="footer">
      <div class="footer__stripe"></div>
      <p class="footer__web">www.hmf-example.org.uk</p>
      <p class="footer__charity">Registered charity No. 1098472</p>
      <p class="footer__phone">
        <svg width="36" height="36" viewBox="0 0 36 36" aria-hidden="true">
          <circle cx="18" cy="18" r="18" fill="#fff"/>
          <path d="M13 9c1.5 0 2.5 3 2.5 4.5S13.5 15 13.5 16c0 2 3.5 6.5 6 7 1 0 1.5-2 2.5-2s4 1.5 4 3-2 3-4 3c-5 0-13-8-13-13 0-3 2.5-5 4-5z" fill="#111"/>
        </svg>
        +44 (0)1632 960418
      </p>
      <div class="footer__social" aria-label="Find us on social media">
        <span></span><span></span>
      </div>
    </footer>
  </main>
</body>
</html>
```